A nerdy designer needs an artistic designer!

Wombridge Devices is an applied research/engineering company - we turn a desired product/capability into something tangible through the application of mathematics, physics, electronics and software engineering. We have a few products of our own, but we also offer contract design services. As a designer, you'd be familiar with our problem - how do you convey what you do when you can do anything a client asks?
Updates

Good evening, Thankyou to all of the designers who have messaged me asking if they can only do the design work (and have someone else perform the site coding) but I don't know how to partition the job into two - i.e. 1. design, 2. coding. The artmarketly site only gave me the options of: 1. web design, or 2. web design + coding (+$150). I chose option #2, because this is what I ultimately need - a functional website. I'll escalate it to the artmarketly helpdesk and ask, but I suspect their answer will be "No. The designer must do both." I sympathise, because there are some things I do well, and some things I don't do at all (like websites). I'll let you know what I learn. Cheers, J

Target Market(s)

Our audience is predominantly technical, so we'd like to have a site which is easy to navigate and find relevant information without too many visually distracting 'popups'/sliding panes etc.

We've provided a series of photos of past projects/examples, all of which:

a. we own,
b. can be cropped/edited/artistically hacked at will etc

to watermark/pepper the pages with to convey a sense of realism/credibility. They're they're as representative images only and not mandatory. Feel free to use them or ignore them as you wish.

Coding

Coded - Design and coding required

Number of Pages Required

5+ page

Font styles to use
Serif
Sans Serif

Colors

Designer to choose colors to be used in the design.

Requirements
Must have
• Editable text. (i.e. nothing permanently embedded in the graphics as the page(s) are likely to evolve fairly rapidly)
Nice to have
• We're pretty open to ideas. Your artistic eye(s) will far exceed anything us (stereotypically) nerdy folk could suggest!

```html
<!DOCTYPE html>
<html lang="en">
<head>
<meta charset="utf-8">
<title>Wombridge Devices</title>
<link rel="stylesheet" href="https://fonts.googleapis.com/css2?family=Open+Sans:wght@400;600;700&display=swap">
<style>
:root{
  --ink:#111;
  --text:#555;
  --muted:#888;
  --line:#e3e3e3;
  --white:#fff;
  --dark:#1a1716;
  --footer:#140c0d;
  --hero-a:#ece9ea;
  --hero-b:#b9b4b6;
}
*{margin:0;padding:0;box-sizing:border-box}
html,body{width:1200px;height:4202px;overflow:hidden;background:var(--white)}
body{position:relative;font-family:"Open Sans",Arial,sans-serif;color:var(--text)}
.abs{position:absolute}
.center{left:0;width:1200px;text-align:center}

/* header */
.brand{left:171px;top:24px;font-size:20px;font-weight:700;color:var(--ink);display:flex;align-items:center;gap:10px;letter-spacing:.5px}
.brand .dot{width:34px;height:34px;border-radius:50%;background:var(--ink)}
.nav{top:38px;font-size:13px;color:#555;letter-spacing:.3px}
.nav.active{color:var(--ink)}
.nav.active::after{content:"";position:absolute;left:0;right:0;top:36px;height:2px;background:var(--ink)}

/* hero */
.hero{top:86px;left:0;width:1200px;height:671px;background:linear-gradient(100deg,var(--hero-a) 0%,#d8d4d5 50%,var(--hero-b) 100%)}
.hero-title{top:322px;font-size:42px;font-weight:700;color:var(--ink)}
.btn-dark{left:507px;top:404px;width:186px;height:49px;background:var(--ink);color:var(--white);font-size:12px;font-weight:700;display:flex;align-items:center;justify-content:center}
.dots{top:718px;left:570px;display:flex;gap:8px}
.dots span{width:8px;height:8px;border-radius:50%;background:rgba(255,255,255,.7)}

/* sections */
.sec-title{font-size:33px;font-weight:700;color:var(--ink)}
.sec-text{font-size:12.5px;line-height:24px;color:var(--text)}
.photo{position:absolute}
.frame{position:absolute;border:2px solid var(--ink);border-right:none;border-bottom:none}
.frame::after{content:"";position:absolute}
.card-title{font-size:19px;font-weight:600;color:var(--ink);text-align:center;letter-spacing:.5px}
.card-text{font-size:12.5px;line-height:21px;text-align:center;color:var(--text)}

/* about */
.about{top:1559px;left:0;width:1200px;height:730px;background:radial-gradient(ellipse at 30% 40%,#2d2827,var(--dark) 70%)}
.about-mark{left:171px;top:1715px;width:424px;height:447px;display:flex;align-items:center;justify-content:center;gap:18px;color:var(--white);font-size:40px;font-weight:700}
.about-mark .dot{width:40px;height:40px;border-radius:50%;background:var(--white)}
.about-title{left:647px;top:1720px;font-size:33px;line-height:45px;font-weight:700;color:var(--white)}
.about-text{left:647px;top:1822px;width:376px;font-size:12.5px;line-height:24px;color:#bbb;text-align:justify}
.btn-line{left:647px;top:2105px;width:92px;height:49px;border:2px solid var(--white);color:var(--white);font-size:11px;font-weight:700;display:flex;align-items:center;justify-content:center}

.divider{left:173px;top:2956px;width:854px;height:2px;background:var(--line)}
.arrow{top:3370px}

/* footer */
.footer{top:3840px;left:0;width:1200px;height:362px;background:var(--footer);color:#ddd}
.f-brand{left:171px;top:3940px;font-size:20px;font-weight:700;color:var(--white);display:flex;align-items:center;gap:10px}
.f-brand .dot{width:34px;height:34px;border-radius:50%;background:var(--white)}
.f-small{font-size:12px;line-height:23px;color:#ddd}
.f-head{font-size:20px;color:var(--white)}
.f-list{list-style:none;font-size:12px;line-height:24px;color:#ddd}
.f-contact{display:flex;align-items:flex-start;gap:16px;font-size:11.5px;line-height:18px;color:#ddd}
.f-contact svg{flex:none}
.social{display:flex;gap:22px}
.social span{width:22px;height:22px;background:var(--white);border-radius:3px}
</style>
</head>
<body>

<header>
  <div class="abs brand"><span class="dot"></span>WOMBRIDGE DEVICES</div>
  <nav>
    <a class="abs nav active" style="left:494px">HOME</a>
    <a class="abs nav" style="left:579px">ABOUT</a>
    <a class="abs nav" style="left:670px">PRODUCT</a>
    <a class="abs nav" style="left:777px">SERVICES</a>
    <a class="abs nav" style="left:882px">NEWS</a>
    <a class="abs nav" style="left:965px">CONTACT</a>
  </nav>
</header>

<section>
  <div class="abs hero" role="img" aria-label="Gloved hands of a lab technician operating an analytical instrument"></div>
  <h1 class="abs center hero-title">WOMBRIDGE DEVICES</h1>
  <a class="abs btn-dark">VIEW OUR INSTRUMENTS</a>
  <div class="abs dots"><span></span><span></span><span></span><span></span></div>
</section>

<section>
  <h2 class="abs center sec-title" style="top:815px">CONTRACT SERVICES</h2>
  <p class="abs sec-text" style="left:330px;width:540px;top:886px;text-align:center">Sed ut perspiciatis unde omnis iste natus error sit voluptatem accusantium doloremque laudantium, totam rem aperiam, eaque ipsa quae ab illo inventore veritatis et quasi architecto beatae vitae dicta sunt explicabo. Nemo enim ipsam voluptatem quia voluptas sit as.</p>

  <div class="frame" style="left:155px;top:1011px;width:218px;height:217px"></div>
  <div class="abs" style="left:155px;top:1011px;width:2px;height:217px;background:var(--ink)"></div>
  <div class="abs" style="left:371px;top:1011px;width:2px;height:21px;background:var(--ink)"></div>
  <div class="abs" style="left:155px;top:1226px;width:18px;height:2px;background:var(--ink)"></div>
  <div class="photo" style="left:173px;top:1032px;width:406px;height:342px;background:linear-gradient(135deg,#c9c49a,#b8bcc0 60%,#8e9aa6)" role="img" aria-label="Hand loading sample vials into an autosampler"></div>
  <h3 class="abs card-title" style="left:173px;width:406px;top:1396px">RESEARCH COMPANY</h3>
  <p class="abs card-text" style="left:223px;width:306px;top:1432px">Sed ut perspiciatis unde omnis iste natus error sit voluptatem accusantium doloremque lauda</p>

  <div class="frame" style="left:598px;top:1011px;width:219px;height:217px"></div>
  <div class="abs" style="left:815px;top:1011px;width:2px;height:21px;background:var(--ink)"></div>
  <div class="abs" style="left:598px;top:1226px;width:22px;height:2px;background:var(--ink)"></div>
  <div class="photo" style="left:620px;top:1032px;width:405px;height:342px;background:linear-gradient(135deg,#dcdcdc,#f2f2f2 55%,#a8a8a8)" role="img" aria-label="Two engineers working at laboratory instruments"></div>
  <h3 class="abs card-title" style="left:620px;width:405px;top:1396px">ENGINEERING COMPANY</h3>
  <p class="abs card-text" style="left:670px;width:306px;top:1432px">Sed ut perspiciatis unde omnis iste natus error sit voluptatem accusantium doloremque lauda</p>
</section>

<section>
  <div class="abs about" role="img" aria-label="Darkened city skyline behind the company name"></div>
  <div class="abs about-mark"><span class="dot"></span>WOMBRIDGE</div>
  <h2 class="abs about-title">ABOUT WOMBRIDGE<br>DEVICES</h2>
  <p class="abs about-text">Sed ut perspiciatis unde omnis iste natus error sit voluptatem accusantium doloremque laudantium, totam rem aperiam, eaque ipsa quae ab illo inventore veritatis et quasi architecto beatae vitae dicta sunt explicabo. Nemo enim ipsam voluptatem quia voluptas sit aspernatur aut odit aut fugit, sed quia consequuntur magni dolores eos qui ratione voluptatem sequi nesciunt. Neque porro quisquam est, qui dolorem ipsum quia dolor sit amet, consectetur, adipisci velit, sed quia non numquam eius modi tempora incidunt ut labore et dolore magnaed ut perspiciatis unde omnis iste natus error sit voluptatem accusantium doloremque laudantium, totam rem aperiam, eaque ipsa quae ab illo inventore.</p>
  <a class="abs btn-line">READ MORE</a>
</section>

<section>
  <h2 class="abs center sec-title" style="top:2352px">OUR PRODUCTS</h2>
  <p class="abs sec-text" style="left:330px;width:540px;top:2424px;text-align:center">Sed ut perspiciatis unde omnis iste natus error sit voluptatem accusantium doloremque laudantium, totam rem aperiam, eaque ipsa quae ab illo inventore verita.</p>

  <div class="photo" style="left:173px;top:2525px;width:195px;height:247px;background:linear-gradient(160deg,#e6e6e6,#bfc6c4 60%,#5f8c80)" role="img" aria-label="Chromatography instrument stack"></div>
  <div class="photo" style="left:393px;top:2525px;width:196px;height:247px;background:linear-gradient(180deg,#f1f1f1,#c9ccd2 60%,#4a5678)" role="img" aria-label="Carousel of sample vials"></div>
  <div class="photo" style="left:611px;top:2525px;width:196px;height:247px;background:linear-gradient(160deg,#c8b8a8,#9a9a98 55%,#3a3a3a)" role="img" aria-label="Electronic test equipment with cables"></div>
  <div class="photo" style="left:831px;top:2525px;width:196px;height:247px;background:linear-gradient(135deg,#dcdcdc,#f0f0f0 55%,#a5a5a5)" role="img" aria-label="Engineers at a computer workstation"></div>

  <h3 class="abs card-title" style="left:173px;width:195px;top:2789px;font-size:17px">MATHEMATICS</h3>
  <h3 class="abs card-title" style="left:393px;width:196px;top:2789px;font-size:17px">PHYSICS</h3>
  <h3 class="abs card-title" style="left:611px;width:196px;top:2789px;font-size:17px">ELECTRONICS</h3>
  <h3 class="abs card-title" style="left:831px;width:196px;top:2789px;font-size:17px">SOFTWARE</h3>
  <p class="abs card-text" style="left:183px;width:175px;top:2826px;font-size:11.5px;line-height:19px">Sed ut perspiciatis unde omnis iste natus er sit voluptatea</p>
  <p class="abs card-text" style="left:403px;width:176px;top:2826px;font-size:11.5px;line-height:19px">Sed ut perspiciatis unde omnis iste natus er sit voluptatea</p>
  <p class="abs card-text" style="left:621px;width:176px;top:2826px;font-size:11.5px;line-height:19px">Sed ut perspiciatis unde omnis iste natus er sit voluptatea</p>
  <p class="abs card-text" style="left:841px;width:176px;top:2826px;font-size:11.5px;line-height:19px">Sed ut perspiciatis unde omnis iste natus er sit voluptatea</p>
</section>

<div class="abs divider"></div>

<section>
  <h2 class="abs center sec-title" style="top:3022px">NEWS &amp; EVENTS</h2>
  <p class="abs sec-text" style="left:330px;width:540px;top:3093px;text-align:center">Sed ut perspiciatis unde omnis iste natus error sit voluptatem accusantium doloremque laudantium, totam rem aperiam, eaque ipsa quae ab illo inventore verita.</p>

  <svg class="abs arrow" style="left:200px" width="26" height="78" viewBox="0 0 26 78"><polyline points="24,1 2,39 24,77" fill="none" stroke="#222" stroke-width="2"/></svg>
  <div class="photo" style="left:277px;top:3187px;width:646px;height:445px;background:linear-gradient(150deg,#f4f4f4,#c9c9cc 50%,#8c8f99)" role="img" aria-label="Autosampler tray with blue-capped vials"></div>
  <svg class="abs arrow" style="left:966px" width="26" height="78" viewBox="0 0 26 78"><polyline points="2,1 24,39 2,77" fill="none" stroke="#222" stroke-width="2"/></svg>

  <p class="abs center" style="top:3673px;font-size:19px;line-height:30px;font-weight:600;color:#333">Sed ut perspiciatis unde omnis iste natuduour sitvo<br>tatem accusantium doloremue laudantium</p>
  <p class="abs center" style="top:3756px;font-size:11px;color:var(--muted)">
    <svg width="13" height="12" viewBox="0 0 13 12" style="vertical-align:-1px"><rect x="1" y="2" width="11" height="9" fill="none" stroke="#999"/><line x1="1" y1="5" x2="12" y2="5" stroke="#999"/></svg> Dec 25 2019</p>
</section>

<footer>
  <div class="abs footer"></div>
  <div class="abs f-brand"><span class="dot"></span>WOMBRIDGE</div>
  <p class="abs f-small" style="left:176px;top:4020px">© 2019 All Rights Are Reserved.<br>Terms of Use | Privacy Policy</p>

  <h4 class="abs f-head" style="left:456px;top:3920px">Links</h4>
  <ul class="abs f-list" style="left:456px;top:3964px">
    <li>Home</li><li>About</li><li>Products</li><li>Services</li><li>News</li><li>Contact</li>
  </ul>

  <h4 class="abs f-head" style="left:623px;top:3920px">Contact Us</h4>
  <div class="abs f-contact" style="left:623px;top:3966px">
    <svg width="18" height="22" viewBox="0 0 18 22"><path d="M9 21C4 14 2 11 2 8a7 7 0 0 1 14 0c0 3-2 6-7 13z" fill="none" stroke="#ddd" stroke-width="1.4"/><circle cx="9" cy="8" r="2.5" fill="none" stroke="#ddd" stroke-width="1.4"/></svg>
    <span>12 Harrow Lane,<br>Eastbrook, Westfield</span>
  </div>
  <div class="abs f-contact" style="left:623px;top:4020px">
    <svg width="22" height="22" viewBox="0 0 22 22"><path d="M5 2l4 4-2 3c1 3 3 5 6 6l3-2 4 4-3 3C9 20 2 13 2 5z" fill="none" stroke="#ddd" stroke-width="1.4"/></svg>
    <span>8 800 555 014 22<br>8 800 555 071 39</span>
  </div>
  <div class="abs f-contact" style="left:623px;top:4075px">
    <svg width="24" height="18" viewBox="0 0 24 18"><rect x="1" y="1" width="22" height="16" fill="none" stroke="#ddd" stroke-width="1.4"/><polyline points="1,1 12,10 23,1" fill="none" stroke="#ddd" stroke-width="1.4"/></svg>
    <span>info@wombridge.test<br>founder@wombridge.test</span>
  </div>

  <h4 class="abs f-head" style="left:884px;top:3920px">Follow Us</h4>
  <div class="abs social" style="left:884px;top:3978px"><span></span><span></span><span></span><span></span></div>
</footer>

</body>
</html>
```